Letterhead design for business

Looking for an attractive and professional letterhead that uses the logo that is attached below.

Target Market(s)

Potential bankruptcy clients.

Industry/Entity Type

Legal

Colors

Designer to choose colors to be used in the design.

Requirements
Must have
• Address for locations, phone number, and website address.
• Addresses are on website larkmoorfirm.legal. Use following phone number (for tracking purposes): 404-731-2864

```html
<!DOCTYPE html>
<html lang="en">
<head>
<meta charset="utf-8">
<title>Larkmoor Law Group – Letterhead &amp; Folder</title>
<link href="https://fonts.googleapis.com/css2?family=Questrial&family=Lato:wght@400;700&display=swap" rel="stylesheet">
<style>
  :root {
    --green: #8cc492;
    --green-dark: #6fb277;
    --ink: #2f2f2f;
    --text: #3a3a3a;
    --rule: #333333;
    --paper: #ffffff;
    --folder: #f1f1f1;
    --bg: #ececec;
    --faint: rgba(0,0,0,0.07);
  }
  * { margin: 0; padding: 0; box-sizing: border-box; }
  html, body { width: 1200px; height: 894px; overflow: hidden; background: var(--bg); }
  body { position: relative; font-family: "Questrial", sans-serif; color: var(--text); }

  .letterhead {
    position: absolute; left: 74px; top: 74px; width: 521px; height: 673px;
    background: var(--paper);
  }
  .band { position: absolute; left: 0; width: 100%; height: 10px; background: var(--green); }
  .band--top { top: 0; }
  .band--bottom { bottom: 0; }

  .brand {
    position: absolute; left: 0; right: 0; top: 34px; text-align: center;
    font-family: "Questrial", sans-serif; color: var(--ink);
  }
  .brand-name { font-size: 24px; letter-spacing: 0.5px; line-height: 1; }
  .brand-sub { font-size: 9px; letter-spacing: 2px; margin-top: 6px; }
  .brand-by { font-size: 8px; margin-top: 3px; color: var(--ink); }

  .rule { position: absolute; left: 45px; right: 45px; height: 1px; background: var(--rule); }
  .rule--head { top: 98px; }
  .rule--foot { top: 617px; }

  .site {
    position: absolute; left: 0; right: 0; top: 104px; text-align: center;
    font-family: "Lato", sans-serif; font-weight: 700; font-size: 9px; letter-spacing: 3px; color: #111;
  }
  .site .site-domain { color: var(--green); font-weight: 400; }

  .body-copy {
    position: absolute; left: 55px; width: 411px; top: 138px;
    font-size: 10.6px; line-height: 17px; text-align: justify; color: var(--text);
  }
  .body-copy p + p { margin-top: 17px; }

  .watermark {
    position: absolute; left: 0; right: 0; top: 318px; text-align: center;
    font-size: 40px; color: var(--faint); letter-spacing: 1px;
  }

  .sign-brand {
    position: absolute; left: 45px; top: 552px; color: #c4c4c4;
    font-size: 18px; line-height: 1;
  }
  .sign-brand small { display: block; font-size: 7px; letter-spacing: 2px; margin-top: 5px; }

  .signature { position: absolute; left: 380px; top: 563px; }
  .signature-name { font-size: 14px; color: var(--ink); }
  .signature-role { font-size: 9.5px; color: var(--ink); margin-top: 8px; }

  .contact {
    position: absolute; left: 45px; top: 633px; font-family: "Lato", sans-serif; font-size: 7.4px; line-height: 12px; color: #222;
  }
  .contact dt { float: left; clear: left; width: 26px; color: var(--green-dark); font-weight: 700; }
  .contact dd { margin-left: 26px; }

  .locations {
    position: absolute; right: 45px; top: 630px; text-align: right;
    font-family: "Lato", sans-serif; font-size: 6.4px; line-height: 12.5px; color: var(--green-dark);
  }

  .folder {
    position: absolute; left: 638px; top: 72px; width: 498px; height: 676px;
    background: var(--folder); border-radius: 14px; overflow: hidden;
  }
  .folder-deco {
    position: absolute; left: 200px; top: 270px; width: 420px; height: 420px;
    border-radius: 50%; background: rgba(140,196,146,0.12);
  }
  .folder-brand {
    position: absolute; left: 108px; top: 528px; color: var(--ink);
  }
  .folder-mark {
    position: absolute; left: 0; top: 8px; width: 64px; height: 64px; border-radius: 50%;
    background: var(--green);
  }
  .folder-text { position: absolute; left: 90px; top: 0; width: 260px; }
  .folder-name { font-size: 36px; line-height: 1; }
  .folder-sub { font-size: 13px; letter-spacing: 3px; margin-top: 8px; }
  .folder-by { font-size: 11px; margin-top: 4px; }
</style>
</head>
<body>
  <article class="letterhead">
    <div class="band band--top"></div>

    <header class="brand">
      <div class="brand-name">Larkmoor</div>
      <div class="brand-sub">LAW GROUP</div>
      <div class="brand-by">by Attorney R. Vantrell</div>
    </header>
    <div class="rule rule--head"></div>
    <div class="site">www.<span class="site-domain">larkmoorfirm</span>.legal</div>

    <div class="watermark" aria-hidden="true">Larkmoor</div>

    <section class="body-copy">
      <p>Lorem ipsum dolor sit amet, consectetur adipiscing elit. Donec orci purus, luctus vitae dignissim eu, iaculis sed purus. Vivamus faucibus, ipsum nec aliquet viverra, leo mauris condimentum ligula, sit amet sagittis enim ligula quis arcu. Nam egestas tortor id nisi porttitor mattis. In tortor ante, ultricies in suscipit a, tempus non massa. Vivamus et auctor mi. Fusce vel massa nulla. Phasellus nec eros mauris, et scelerisque orci. Donec malesuada orci vitae nulla accumsan porta a id massa.</p>
      <p>Quisque accumsan iaculis magna sit amet fringilla. Maecenas consequat, magna eget tincidunt semper, odio nibh rutrum mi, id feugiat ante nisi eu risus. Vestibulum nunc orci, rhoncus a placerat in, ultricies in mi. Cras mattis varius eros, vel fringilla nisi suscipit eget. Quisque scelerisque sagittis nulla at porttitor. Mauris a justo et tellus interdum tristique. Sed id augue vitae urna euismod commodo aliquet a quam. Pellentesque arcu velit, cursus et malesuada ut, consequat et diam. Nullam erat sem, rhoncus id ullamcorper vitae, rhoncus et arcu. In ultricies ultricies nulla.</p>
      <p>Kut rutrum nisi iaculis at. Donec eu magna a metus ornare faucibus. Fusce aliquet faucibus ultricies. Morbi semper, est id tincidunt gravida, sem arcu adipiscing lacus, ac bibendum nulla leo eu purus. Quisque nec diam sed risus consectetur a ccumsan quis quis nibh. Vestibulum id purus lorem. Donec eu magna a metus ornare faucibus. Fusce aliquet faucibus ultricies. Morbi semper, est id tincidunt gravida, sem arcu adipiscing lacus, ac bibendum nulla leo eu purus. Quisque nec diam sed risus consectetur a ccumsan quis quis nibh. Vestibulum id purus lorem.</p>
    </section>

    <div class="sign-brand">Larkmoor<small>LAW GROUP</small></div>
    <div class="signature">
      <div class="signature-name">Owen Hale</div>
      <div class="signature-role">Co-Founder &amp; CEO</div>
    </div>

    <div class="rule rule--foot"></div>
    <dl class="contact">
      <dt>Tel:</dt><dd>404.731.2864</dd>
      <dt>Email:</dt><dd>info@larkmoorfirm.legal</dd>
    </dl>
    <address class="locations">
      4120 Elm Ridge Ave. Marrow, Georgia 30277<br>
      815 Halvern St., NW Suite #1400 Atlanta, Georgia 30308
    </address>

    <div class="band band--bottom"></div>
  </article>

  <aside class="folder">
    <div class="folder-deco" aria-hidden="true"></div>
    <div class="folder-brand">
      <div class="folder-mark" aria-hidden="true"></div>
      <div class="folder-text">
        <div class="folder-name">Larkmoor</div>
        <div class="folder-sub">LAW GROUP</div>
        <div class="folder-by">by Attorney R. Vantrell</div>
      </div>
    </div>
  </aside>
</body>
</html>
```